skincare creams for tired moms

I need a package and a logo design for a skincare company based in California called Lumen Petal. I make day and night cream, under eye cream, and body lotion. The first product I plan to launch is an under eye cream. It does not have to be in these colors but I do teals, greens, black, and cobalt blue.

The package is going to either be in a box or a bag. Either way I go it will be like a gift box or bag. The design should make the person feel like they are getting something special and luxurious just for them.

I have small kids and it is really difficult to find a chunk of time to myself to update or review.

Target Market(s)

mainly first time moms. I am making an under eye cream that does not use retinol but is still powerful enough to get rid of bags and dark circles.

Industry/Entity Type

Cosmetics

Logo Text

The package and logo should incorporate the name Lumen Petal.

Font styles to use
Decorative
Script

Colors

Designer to choose colors to be used in the design.

Requirements
Nice to have
• maybe focus more on Petal instead of Lumen. Also incorporate plants or flowers
Should not have
• not a huge fan of pink

```html
<!DOCTYPE html>
<html lang="en">
<head>
<meta charset="utf-8">
<title>Lumen Petal Eye Repair Cream Packaging</title>
<link href="https://fonts.googleapis.com/css2?family=Questrial&family=Pinyon+Script&display=swap" rel="stylesheet">
<style>
  :root {
    --bg: #ffffff;
    --panel-top: #e3e8ed;
    --panel-mid: #f4f6f5;
    --ink: #2b2b2b;
    --ink-soft: #4a4a4a;
    --wash: #e6efcf;
    --leaf-light: #c9de8a;
    --leaf: #8fb84a;
    --leaf-deep: #4f8a2e;
    --cap: #111111;
  }
  * { margin: 0; padding: 0; box-sizing: border-box; }
  html, body { width: 1200px; height: 1200px; overflow: hidden; background: var(--bg); }
  body { position: relative; font-family: "Questrial", sans-serif; color: var(--ink); }

  .box-side, .box-front, .bottle-label { position: absolute; overflow: hidden; }

  .box-side {
    left: 150px; top: 300px; width: 130px; height: 620px;
    background: linear-gradient(180deg, #fbfbfb 0%, #f4f5f4 60%, var(--wash) 100%);
    border-right: 1px solid #dfe3e6;
    padding: 70px 10px 0 12px;
  }
  .side-copy {
    font-size: 7.4px; line-height: 13px; color: var(--ink-soft);
    text-align: justify; margin-bottom: 14px;
  }

  .box-front {
    left: 280px; top: 300px; width: 300px; height: 620px;
    background: linear-gradient(180deg, var(--panel-top) 0%, var(--panel-mid) 45%, #f7f9f2 60%, var(--wash) 75%);
    text-align: center;
  }
  .bottle-label {
    left: 680px; top: 420px; width: 260px; height: 500px;
    background: linear-gradient(180deg, #ffffff 0%, #f6f7f4 40%, var(--wash) 60%);
    text-align: center;
    border-top: 26px solid var(--cap);
  }

  .brand-mark {
    width: 60px; height: 60px; border: 2px solid var(--ink);
    border-radius: 50%; margin: 0 auto 14px;
  }
  .brand-name { font-size: 21px; letter-spacing: 0.5px; color: var(--ink); }

  .product-title { font-size: 29px; letter-spacing: 0.5px; color: var(--ink); }
  .product-sub {
    font-family: "Pinyon Script", cursive; font-size: 30px; color: var(--ink); line-height: 1;
  }
  .ingredients {
    font-size: 11px; font-style: italic; line-height: 17px; color: var(--ink-soft);
  }
  .volume { font-size: 13px; color: var(--ink-soft); position: absolute; left: 0; right: 0; }

  .floral-art {
    position: absolute; left: 0; right: 0; bottom: 0;
    background:
      radial-gradient(ellipse at 70% 55%, rgba(255,255,255,0.9) 0 12%, transparent 30%),
      radial-gradient(ellipse at 25% 70%, var(--leaf) 0%, transparent 45%),
      linear-gradient(180deg, rgba(201,222,138,0) 0%, var(--leaf-light) 35%, var(--leaf) 75%, var(--leaf-deep) 100%);
  }

  .box-front .brand-mark { margin-top: 45px; }
  .box-front .product-title { margin-top: 90px; }
  .box-front .product-sub { margin-top: 12px; }
  .box-front .ingredients { margin-top: 100px; }
  .box-front .floral-art { height: 280px; }
  .box-front .volume { bottom: 40px; z-index: 1; }

  .box-side .floral-art { height: 240px; opacity: 0.85; }

  .bottle-label .brand-mark { margin-top: 40px; width: 56px; height: 56px; }
  .bottle-label .brand-name { font-size: 19px; }
  .bottle-label .product-title { margin-top: 28px; font-size: 27px; }
  .bottle-label .product-sub { margin-top: 6px; font-size: 28px; }
  .bottle-label .floral-art { height: 260px; }
  .bottle-label .volume { bottom: 36px; z-index: 1; font-size: 12px; }
</style>
</head>
<body>
  <section class="box-side">
    <p class="side-copy">Our gentle eye cream is made in small batches with green tea, arnica and soothing peptides to brighten tired eyes. Smooth a small amount under each eye every morning and night, patting lightly until fully absorbed.</p>
    <p class="side-copy">Store in a cool, dry place away from sunlight. For external use only. Avoid direct contact with eyes. Stop use if irritation occurs.</p>
    <div class="floral-art" role="img" aria-label="Watercolour green leaves and small white flowers"></div>
  </section>

  <section class="box-front">
    <div class="brand-mark"></div>
    <div class="brand-name">Lumen Petal</div>
    <h1 class="product-title">EYE REPAIR</h1>
    <div class="product-sub">Cream</div>
    <p class="ingredients">90% Green Tea Polyphenols<br>Arnica, Vitamin K, &amp; Peptides</p>
    <div class="floral-art" role="img" aria-label="Watercolour green wash with leaves and white lilies"></div>
    <div class="volume">0.5 fl Oz / 15ml</div>
  </section>

  <section class="bottle-label">
    <div class="brand-mark"></div>
    <div class="brand-name">Lumen Petal</div>
    <h2 class="product-title">EYE REPAIR</h2>
    <div class="product-sub">Cream</div>
    <div class="floral-art" role="img" aria-label="Watercolour green leaves and small white flowers"></div>
    <div class="volume">0.5 fl Oz / 15ml</div>
  </section>
</body>
</html>
```